Business Card Design

I need a business card designed for my new company BrightOak Home developments I specialise in all aspects of carpentry including Decks, Pergolas, Conventional Framing and fit outs I am open to different colours as long as it fits with my logo.

Industry/Entity Type

Carpentry

Contact Information for Business Card

BrightOak Home Developments, Rob Keltmore, 0481604328, specialising in all aspects of carpentry and construction

```html
<!DOCTYPE html>
<html lang="en">
<head>
<meta charset="utf-8">
<title>BrightOak Home Developments – Business Card</title>
<link rel="stylesheet" href="https://fonts.googleapis.com/css2?family=Open+Sans:wght@400;600;700&display=swap">
<style>
  :root {
    --bg: #e9e7e4;
    --card-black: #141718;
    --card-charcoal: #2a2e30;
    --card-white: #ffffff;
    --brand-blue: #2f7fd0;
    --brand-blue-dark: #1f5ea8;
    --logo-blue: #4a7fc4;
    --text-light: #e8eaeb;
  }
  * { box-sizing: border-box; margin: 0; padding: 0; }
  html, body {
    width: 1200px; height: 800px; overflow: hidden;
    background: var(--bg);
    font-family: "Open Sans", Arial, sans-serif;
  }
  .canvas { position: relative; width: 1200px; height: 800px; }

  /* Back of card (portrait) */
  .card-back {
    position: absolute; left: 110px; top: 130px;
    width: 320px; height: 540px;
    background: var(--card-black);
    box-shadow: 0 10px 30px rgba(0,0,0,.25);
    overflow: hidden;
  }
  .card-back .star-decoration {
    position: absolute; inset: 0;
    background: radial-gradient(ellipse at 55% 45%, var(--card-charcoal) 0%, var(--card-black) 70%);
  }
  .card-back .brand-name {
    position: absolute; left: 0; right: 0; top: 215px;
    text-align: center; color: var(--text-light);
    font-weight: 400; font-size: 26px; letter-spacing: 3px; line-height: 1.35;
    text-transform: uppercase;
  }

  /* Front of card (landscape) */
  .card-front {
    position: absolute; left: 500px; top: 225px;
    width: 620px; height: 354px;
    background: var(--card-black);
    box-shadow: 0 10px 30px rgba(0,0,0,.25);
    overflow: hidden;
  }
  .card-front .top-panel {
    position: absolute; left: 0; top: 0; width: 100%; height: 138px;
    background: var(--card-white);
  }
  .card-front .brand-name {
    position: absolute; right: 36px; top: 42px;
    color: var(--logo-blue); font-weight: 400;
    font-size: 30px; letter-spacing: 2px; line-height: 1.25;
    text-transform: uppercase; text-align: right;
  }
  .card-front .tagline-band {
    position: absolute; left: 0; top: 138px; width: 100%; height: 22px;
    background: linear-gradient(90deg, var(--brand-blue-dark), var(--brand-blue));
    color: #fff; font-weight: 700; font-size: 11.5px; letter-spacing: .6px;
    line-height: 22px; text-transform: uppercase; text-align: right; padding-right: 24px;
  }
  .card-front .contact {
    position: absolute; left: 28px; top: 176px; color: var(--text-light);
  }
  .contact .person-name {
    color: var(--brand-blue); font-weight: 700; font-size: 19px;
    letter-spacing: .5px; text-transform: uppercase;
  }
  .contact .person-role { font-size: 13px; margin: 2px 0 8px; }
  .contact .contact-line {
    display: flex; align-items: center; gap: 8px;
    font-size: 12.5px; line-height: 19px;
  }
  .contact .contact-line svg { width: 11px; height: 11px; flex: none; }
  .contact .postal {
    color: var(--brand-blue); font-weight: 700; font-size: 13px;
    margin-top: 8px; text-transform: uppercase;
  }
  .card-front .star-decoration {
    position: absolute; right: 0; bottom: 0; width: 300px; height: 190px;
    background: radial-gradient(ellipse at 70% 65%, #25292b 0%, var(--card-black) 70%);
  }
</style>
</head>
<body>
<main class="canvas">

  <section class="card-back" aria-label="Business card back">
    <div class="star-decoration" role="img" aria-label="Faint large star shape decoration"></div>
    <p class="brand-name">BrightOak<br>Home<br>Developments</p>
  </section>

  <section class="card-front" aria-label="Business card front">
    <div class="top-panel">
      <p class="brand-name">BrightOak<br>Home Developments</p>
    </div>
    <div class="tagline-band">Specialising in all aspects of carpentry and construction</div>
    <div class="star-decoration" role="img" aria-label="Scattered outline shooting stars decoration"></div>
    <div class="contact">
      <p class="person-name">Rob Keltmore</p>
      <p class="person-role">Director</p>
      <p class="contact-line">
        <svg viewBox="0 0 12 12"><rect width="12" height="12" rx="2" fill="#2f7fd0"/><rect x="4" y="2" width="4" height="8" rx="1" fill="#fff"/></svg>
        0481 604 328
      </p>
      <p class="contact-line">
        <svg viewBox="0 0 12 12"><rect width="12" height="12" rx="2" fill="#2f7fd0"/><rect x="2" y="3.5" width="8" height="5" fill="#fff"/><path d="M2 3.5 6 6.5 10 3.5" stroke="#2f7fd0" fill="none"/></svg>
        rob@brightoakhomes.com.au
      </p>
      <p class="contact-line">
        <svg viewBox="0 0 12 12"><rect width="12" height="12" rx="2" fill="#2f7fd0"/><circle cx="6" cy="6" r="3.5" stroke="#fff" fill="none"/><path d="M2.5 6h7M6 2.5v7" stroke="#fff" stroke-width=".8"/></svg>
        www.brightoakhomes.com.au
      </p>
      <p class="postal">PO Box 278 Greenvale BC 1520</p>
    </div>
  </section>

</main>
</body>
</html>
```